Brochure Design Project -postcard size 1/4 of A4 sheet

We are a bright and happening cafe which is an old milk bar converted into a cafe. I need to have a postcard designed for letterbox drop to let locals know what great food and coffee we have. The postcard ideally would have a black and white old world milk bar scene and a promise of old fashion service in a changing neighborhood.
Here is a little about our place
http://www.nearbyfinder.com.au/business/carlow-lane-corner-store/richmond
I can't seem to put any updates but if you are having trouble with image graphics are ok that depicts an "old world" coffee shoo from 60s or 70s postcard size is a 1/4 of an A4 sheet
http://www.pagecircle.com/group.php?gid=52918473016&v=wall
I am working off an iPad and this website does not allow feedback via iPad so have to put everything in brief link to a PageCircle site now
Updates
Yeyyy !! I have been working off an Ipad which does not allow me to give feedback. I love the old world look of the recent designs I have now attached our logo and a pagecircle site of the cafe for more details.
Many Thanks
Mar la
Target Market(s)
Local community aged mainly 20 to 50
Industry/Entity Type
Fashion
Requirements
Must have
- Black and white image on the front of postcard an old milk bar scene and the words
Carlow lane corner store ....a constant among change
Nice to have
- On the back to read we need to know what you want at your local foodstore
A little about our milk bar can be read at

```html
<!DOCTYPE html>
<html lang="en">
<head>
<meta charset="utf-8">
<title>Carlow Lane Corner Store – Postcard</title>
<link rel="stylesheet" href="https://fonts.googleapis.com/css2?family=Open+Sans:wght@400;700;800&family=Vollkorn:ital,wght@1,700&family=Courier+Prime&display=swap">
<style>
  :root {
    --page-bg: #ece7df;
    --wood-light: #f3dfb8;
    --wood-mid: #e8c894;
    --brown-dark: #4a2e1a;
    --brown-mid: #6b4426;
    --cream: #f7efc9;
    --pink: #f2b9cb;
    --pink-light: #f8d3df;
    --ink: #2b1c12;
    --label: #222;
    --illustration-light: #f4f2ee;
    --illustration-grey: #b9b4ad;
  }
  * { box-sizing: border-box; margin: 0; padding: 0; }
  html, body { width: 1200px; height: 900px; overflow: hidden; }
  body { background: var(--page-bg); position: relative; font-family: "Open Sans", sans-serif; }

  .postcard { position: absolute; width: 540px; height: 383px; overflow: hidden; box-shadow: 0 3px 10px rgba(0,0,0,.18); }
  .postcard--front { left: 40px; top: 60px; background: linear-gradient(160deg, var(--wood-light), var(--wood-mid)); }
  .postcard--back { left: 620px; top: 420px; background: radial-gradient(circle at 40% 60%, var(--pink-light), var(--pink) 70%); }

  .side-label { position: absolute; font-size: 18px; color: var(--label); letter-spacing: .5px; }
  .side-label--front { left: 58px; top: 458px; }
  .side-label--back { left: 638px; top: 818px; }

  .brand { position: absolute; display: flex; align-items: center; gap: 8px; }
  .brand__name { font-weight: 800; color: var(--brown-dark); line-height: 1; text-transform: uppercase; }
  .brand__mark { width: 22px; height: 22px; background: var(--cream); border: 2px solid var(--brown-dark); flex: none; }
  .postcard--front .brand { left: 22px; top: 20px; }
  .postcard--front .brand__name { font-size: 22px; width: 180px; }
  .tagline { position: absolute; left: 34px; top: 74px; font-weight: 700; font-size: 13px; color: var(--brown-mid); }

  .offer { position: absolute; left: 30px; width: 218px; }
  .offer__title, .review__title { font-family: "Vollkorn", serif; font-style: italic; font-weight: 700; color: var(--brown-dark); font-size: 17px; line-height: 1.1; }
  .offer__text { font-size: 11px; line-height: 1.4; color: var(--brown-mid); }
  .offer--coffee { top: 108px; }
  .offer--lunch { top: 186px; }
  .offer--breakfast { top: 272px; }

  .storefront { position: absolute; left: 250px; top: 60px; width: 268px; height: 280px; background: linear-gradient(180deg, var(--illustration-light), #dcd8d1); border: 1px solid var(--illustration-grey); }

  .address-badge { position: absolute; left: 330px; top: 228px; width: 128px; height: 128px; border-radius: 50%; background: var(--brown-dark); box-shadow: 0 0 0 5px var(--cream); color: var(--cream); display: flex; flex-direction: column; align-items: center; justify-content: center; text-align: center; line-height: 1.2; }
  .address-badge__street { font-size: 15px; }
  .address-badge__suburb { font-size: 11px; }
  .address-badge__phone { font-size: 13px; margin-top: 2px; }

  .postcard--back .brand { right: 22px; top: 22px; flex-direction: row-reverse; }
  .postcard--back .brand__name { font-size: 24px; width: 190px; text-align: right; }

  .waitress { position: absolute; left: 0; bottom: 0; width: 190px; height: 230px; background: linear-gradient(180deg, #d9d4d0, #6f6a66); }

  .review { position: absolute; }
  .review__quote { font-family: "Courier Prime", monospace; font-size: 11px; line-height: 1.35; color: var(--ink); }
  .review--friendly { left: 36px; top: 26px; width: 290px; }
  .review--secret { left: 216px; top: 138px; width: 300px; }
  .review--affordable { left: 206px; top: 230px; width: 300px; }
  .back-contact { position: absolute; left: 200px; bottom: 20px; font-size: 12px; color: var(--ink); }
</style>
</head>
<body>

  <section class="postcard postcard--front" aria-label="Postcard front">
    <div class="brand">
      <span class="brand__name">Carlow Lane Corner Store</span>
      <span class="brand__mark"></span>
    </div>
    <p class="tagline">...a constant among change</p>

    <div class="offer offer--coffee">
      <h3 class="offer__title">Coffee</h3>
      <p class="offer__text">We offer an extensive breakfast range and great tasting coffee.</p>
    </div>
    <div class="offer offer--lunch">
      <h3 class="offer__title">Lunch</h3>
      <p class="offer__text">Wide selection of lunch options. The ideal location for a casual catch up with friends or a working lunch.</p>
    </div>
    <div class="offer offer--breakfast">
      <h3 class="offer__title">Breakfast</h3>
      <p class="offer__text">Hip and kid friendly we have a couple of long 8 seater tables. Ideal for the big extended family breakfast or lunch.</p>
    </div>

    <div class="storefront" role="img" aria-label="Black and white line drawing of an old corner store shopfront with coffee and breakfast signage"></div>

    <div class="address-badge">
      <span class="address-badge__street">14 Carlow Ln</span>
      <span class="address-badge__suburb">Richmond<br>VIC 3121</span>
      <span class="address-badge__phone">(03) 9555 0172</span>
    </div>
  </section>
  <p class="side-label side-label--front">FRONT</p>

  <section class="postcard postcard--back" aria-label="Postcard back">
    <div class="brand">
      <span class="brand__name">Carlow Lane Corner Store</span>
      <span class="brand__mark"></span>
    </div>

    <div class="review review--friendly">
      <h3 class="review__title">Hip and Friendly</h3>
      <p class="review__quote">“There is a real charm about this place. I’ve lived nearby when it was the local milk bar, useful but not a place you’d want to stop for long. Now it’s a hip cafe.”</p>
    </div>
    <div class="review review--secret">
      <h3 class="review__title">Local Secret</h3>
      <p class="review__quote">“This place is well known to locals but is still a bit of a secret for the rest of Richmond. It also has coffee worth stopping for.”</p>
    </div>
    <div class="review review--affordable">
      <h3 class="review__title">Affordable</h3>
      <p class="review__quote">“Locals know this place well. It’s also family friendly so if you want an affordable breakfast out with your kids and friends all sitting at one big table this is a good place for you.”</p>
    </div>

    <div class="waitress" role="img" aria-label="Black and white retro illustration of a smiling waitress carrying a tray with a milkshake"></div>

    <p class="back-contact">14 Carlow Ln, Richmond, VIC 3121, (03) 9555 0172</p>
  </section>
  <p class="side-label side-label--back">BACK</p>

</body>
</html>
```